TRUCK WASH OUTDOOR DRIVE THROUGH MENU CONTEST

WE NEED A DRIVE THROUGH MENU WITH OUR SERVICES AND PRICES. I HAVE ATTACHED A FEW EXAMPLES THAT I STARTED.

I WANT THIS TO BE EYE CATCHING WITH BRIGHT COLORS

Target Market(s)

TRUCK WASH AND DETAIL SHOP, TRANSPORTATION.

Requirements
Must have
• INCORPORATE MY LOGO INTO THE SIGN.
• FINAL PROJECT MUST BE IN .AI FORMAT.
• COMPANY COLORS ARE RED AND BLUE

```html
<!DOCTYPE html>
<html lang="en">
<head>
<meta charset="utf-8">
<title>Rolling Rig Wash – Drive Through Menu</title>
<link rel="stylesheet" href="https://fonts.googleapis.com/css2?family=Saira+Condensed:wght@600;700&family=Oswald:wght@500&family=Copse&display=swap">
<style>
  :root {
    --wave-light: #8fd3f4;
    --wave-mid: #3aa6e3;
    --wave-deep: #1a73c9;
    --card: #ffffff;
    --brand-red: #e8232f;
    --ink: #111111;
    --navy: #1e3d78;
    --platinum: #efefec;
    --gold: #e3ab23;
    --silver: #c8c8c8;
    --express: #5fd7f5;
  }
  * { box-sizing: border-box; margin: 0; padding: 0; }
  html, body { width: 923px; height: 1200px; overflow: hidden; }
  body { position: relative; font-family: "Copse", serif; color: var(--ink); }

  .wave-backdrop {
    position: absolute; inset: 0;
    background: linear-gradient(160deg, var(--wave-light) 0%, var(--wave-mid) 45%, var(--wave-deep) 75%, var(--wave-mid) 100%);
  }

  .menu-card {
    position: absolute; left: 101px; top: 64px; width: 728px; height: 1062px;
    background: var(--card); border: 4px solid var(--brand-red); border-radius: 32px;
    overflow: hidden;
  }

  .brand-name {
    position: absolute; left: 0; right: 0; top: 150px;
    text-align: center; font-family: "Saira Condensed", sans-serif; font-weight: 700;
    font-size: 64px; line-height: 1; color: var(--brand-red);
  }

  .menu-title {
    position: absolute; left: 0; right: 0; top: 250px;
    text-align: center; font-family: "Saira Condensed", sans-serif; font-weight: 600;
    font-size: 46px; line-height: 1; color: var(--ink);
  }

  .tier {
    position: absolute; left: 0; width: 720px; height: 160px;
  }
  .tier--platinum { top: 330px; background: var(--platinum); }
  .tier--gold     { top: 492px; background: var(--gold); height: 157px; }
  .tier--silver   { top: 649px; background: var(--silver); }
  .tier--express  { top: 809px; background: var(--express); height: 163px; }

  .tier-name, .tier-price {
    position: absolute; top: 22px; font-family: "Oswald", sans-serif; font-weight: 500;
    font-size: 44px; line-height: 1; color: var(--navy); letter-spacing: 0.5px;
  }
  .tier-name { left: 26px; }
  .tier-price { left: 560px; }

  .tier-services {
    position: absolute; left: 252px; top: 16px; list-style: none;
    font-size: 22px; line-height: 27px;
  }
  .tier-services li::before { content: "· "; }

  .menu-footer {
    position: absolute; left: 0; right: 0; top: 996px;
    text-align: center; font-family: "Saira Condensed", sans-serif; font-weight: 600;
    font-size: 21px; color: var(--ink);
  }
</style>
</head>
<body>
  <div class="wave-backdrop" role="img" aria-label="Flowing blue water waves with floating soap bubbles"></div>

  <main class="menu-card">
    <div class="brand-name">Rolling Rig Wash</div>
    <h1 class="menu-title">Standard Tractor &amp; Trailer [53']</h1>

    <section class="tier tier--platinum">
      <h2 class="tier-name">PLATINUM</h2>
      <ul class="tier-services">
        <li>Pre-Soak</li><li>Soap and Scrubb</li><li>Rinse</li><li>Tire Shine</li><li>Platinum Protection</li>
      </ul>
      <p class="tier-price">$130.00</p>
    </section>

    <section class="tier tier--gold">
      <h2 class="tier-name">GOLD</h2>
      <ul class="tier-services">
        <li>Pre-Soak</li><li>Soap and Scrubb</li><li>Rinse</li><li>Tire Shine</li><li>Wet X Polish</li>
      </ul>
      <p class="tier-price">$120.00</p>
    </section>

    <section class="tier tier--silver">
      <h2 class="tier-name">SILVER</h2>
      <ul class="tier-services">
        <li>Pre-Soak</li><li>Soap and Scrubb</li><li>Rinse</li><li>Tire Shine</li>
      </ul>
      <p class="tier-price">$100.00</p>
    </section>

    <section class="tier tier--express">
      <h2 class="tier-name">EXPRESS</h2>
      <ul class="tier-services">
        <li>Pre-Soak</li><li>Soap and Scrubb</li><li>Rinse</li>
      </ul>
      <p class="tier-price">$80.00</p>
    </section>

    <p class="menu-footer">FOR MORE OPTIONS ASK FRONT DESK</p>
  </main>
</body>
</html>
```